Business card for wedding & event planning company

I'm looking for a well designed double sided business card to represent my wedding and event planning company.

It should include the fact we manage the following events:
Weddings, birthdays, conferences, product launches, fashion shows & conventions
in the following areas:
Wiltshire, Oxfordshire, Berkshire & London

My contact details to be included are:

Moira Lintell
07741 308562
moira@amberfinchgatherings.co.uk
www.amberfinchgatherings.co.uk

My logo can be found at the following Filevaultly location:
AI file: https://www.filevaultly.com/s/k3mprt8wq51bn2x/brief_480317_2290451_7735102_sourcefile.ai?dl=0
PNG file:
https://www.filevaultly.com/s/hv7ncqeyb4tlofu/brief_480317_2290451_7735102_e8a1b406_image.png?dl=0

Target Market(s)

women aged 30-55

Industry/Entity Type

Wedding

Contact Information for Business Card

in the following areas:

Moira Lintell
Event Planner
07741 308562

Font styles to use
Serif
Sans Serif
Script

Requirements
Must have
• Purple and white colour scheme
Should not have
• Black background
• Please don't submit any of the see-through business card designs.

```html
<!DOCTYPE html>
<html lang="en">
<head>
<meta charset="utf-8">
<title>Amber Finch Gatherings – Business Card</title>
<link rel="stylesheet" href="https://fonts.googleapis.com/css2?family=Open+Sans:wght@400;600;700&display=swap">
<style>
  :root {
    --stage: #e9e8ec;
    --purple: #8a2f93;
    --purple-deep: #7a2683;
    --white: #ffffff;
    --card-white: #f7f7f7;
    --ink: #111111;
    --rule: #c9b4cc;
    --shadow: rgba(40, 20, 45, 0.18);
  }
  * { margin: 0; padding: 0; box-sizing: border-box; }
  html, body {
    width: 1200px;
    height: 864px;
    overflow: hidden;
    background: var(--stage);
    font-family: "Open Sans", Arial, sans-serif;
  }
  .canvas {
    position: relative;
    width: 1200px;
    height: 864px;
  }
  .card {
    position: absolute;
    width: 620px;
    height: 354px;
    border-radius: 4px;
    box-shadow: 0 10px 28px var(--shadow);
    overflow: hidden;
  }

  /* Reverse side */
  .card--back {
    left: 190px;
    top: 52px;
    background: var(--purple);
    color: var(--white);
    text-align: center;
  }
  .services {
    position: absolute;
    left: 0;
    right: 0;
    top: 78px;
    font-size: 16px;
    line-height: 21px;
  }
  .services__title {
    font-weight: 700;
    font-size: 16px;
  }
  .services__group + .services__group { margin-top: 24px; }

  /* Front side */
  .card--front {
    left: 390px;
    top: 452px;
    background: radial-gradient(ellipse at 35% 40%, var(--white) 0%, var(--card-white) 70%, #ececec 100%);
  }
  .holder-name {
    position: absolute;
    left: 62px;
    top: 136px;
    font-size: 24px;
    font-weight: 700;
    color: var(--purple-deep);
  }
  .brand {
    position: absolute;
    right: 58px;
    top: 104px;
    display: flex;
    align-items: center;
    gap: 12px;
    padding-bottom: 10px;
    border-bottom: 1px solid var(--rule);
  }
  .brand__mark {
    width: 26px;
    height: 26px;
    border-radius: 50%;
    background: var(--purple);
  }
  .brand__name {
    font-size: 23px;
    font-weight: 400;
    color: var(--purple);
    letter-spacing: 0.5px;
  }
  .contacts {
    position: absolute;
    right: 44px;
    top: 232px;
    list-style: none;
  }
  .contacts__item {
    display: flex;
    justify-content: flex-end;
    align-items: center;
    gap: 10px;
    font-size: 16px;
    line-height: 22px;
    color: var(--ink);
    margin-bottom: 4px;
  }
  .contacts__icon {
    width: 20px;
    height: 20px;
    border-radius: 3px;
    background: var(--purple);
    display: flex;
    align-items: center;
    justify-content: center;
  }
  .contacts__icon svg { width: 13px; height: 13px; }
</style>
</head>
<body>
<main class="canvas">

  <section class="card card--back" aria-label="Business card reverse">
    <div class="services">
      <div class="services__group">
        <p class="services__title">Events:</p>
        <p>Weddings | Birthdays | Conferences |</p>
        <p>Product Launches | Fashion Shows</p>
      </div>
      <div class="services__group">
        <p class="services__title">Convention Areas</p>
        <p>Wiltshire | Oxfordshire | Berkshire | London</p>
      </div>
    </div>
  </section>

  <section class="card card--front" aria-label="Business card front">
    <h1 class="holder-name">Moira Lintell</h1>

    <div class="brand">
      <span class="brand__mark" aria-hidden="true"></span>
      <span class="brand__name">Amber Finch Gatherings</span>
    </div>

    <ul class="contacts">
      <li class="contacts__item">
        <span>07741 308562</span>
        <span class="contacts__icon" aria-hidden="true">
          <svg viewBox="0 0 24 24"><path fill="#fff" d="M6.6 10.8a15.1 15.1 0 0 0 6.6 6.6l2.2-2.2a1 1 0 0 1 1-.25 11.4 11.4 0 0 0 3.6.57 1 1 0 0 1 1 1V20a1 1 0 0 1-1 1A17 17 0 0 1 3 4a1 1 0 0 1 1-1h3.5a1 1 0 0 1 1 1c0 1.25.2 2.45.57 3.57a1 1 0 0 1-.25 1z"/></svg>
        </span>
      </li>
      <li class="contacts__item">
        <span>moira@amberfinchgatherings.co.uk</span>
        <span class="contacts__icon" aria-hidden="true">
          <svg viewBox="0 0 24 24"><rect x="2" y="5" width="20" height="14" rx="1.5" fill="#fff"/><path d="M3 6l9 7 9-7" fill="none" stroke="#8a2f93" stroke-width="2"/></svg>
        </span>
      </li>
      <li class="contacts__item">
        <span>www.amberfinchgatherings.co.uk</span>
        <span class="contacts__icon" aria-hidden="true">
          <svg viewBox="0 0 24 24"><g fill="none" stroke="#fff" stroke-width="2.6" stroke-linecap="round"><path d="M10 14l4-4"/><path d="M8.5 11.5l-2.5 2.5a3 3 0 0 0 4 4l2.5-2.5"/><path d="M15.5 12.5l2.5-2.5a3 3 0 0 0-4-4l-2.5 2.5"/></g></svg>
        </span>
      </li>
    </ul>
  </section>

</main>
</body>
</html>
```